Corvane Holdings , new business card design

investment firm with corporate clients . need double sided business card , vertical and horizontal options ,logo must be clear. prefer pantone colors only and sharp design. website also www.corvane-demo.ae

Khalid Bin Rashed
Managing Director
Tel. +971 4 000 1234
Mobile +971 50 000 5678
khalid@corvane-demo.ae
Palmgate Tower, officw 18-B07, Noor Terraces, Dubai

Khalid Bin Rashed
Managing Director

Serif

Designer to choose colors to be used in the design.

```html
<!DOCTYPE html>
<html lang="en">
<head>
<meta charset="utf-8">
<title>Corvane Holdings – Business Card</title>
<link rel="stylesheet" href="https://fonts.googleapis.com/css2?family=Josefin+Sans:wght@300;400;600&display=swap">
<style>
  :root {
    --stage: #1c1c1c;
    --card-dark: #141414;
    --card-light: #efefef;
    --ink: #1e1e1e;
    --ink-soft: #3a3a3a;
    --brand-blue: #3f6d9e;
    --rule: #b5b5b5;
    --white: #ffffff;
  }
  * { box-sizing: border-box; margin: 0; padding: 0; }
  html, body {
    width: 1200px; height: 900px; overflow: hidden;
    background: var(--stage);
    font-family: "Josefin Sans", "Century Gothic", sans-serif;
  }
  .stage {
    position: relative; width: 1200px; height: 900px;
    display: flex; flex-direction: column; align-items: center; justify-content: center; gap: 40px;
  }
  .card {
    position: relative; width: 560px; height: 320px; border-radius: 22px; overflow: hidden;
  }
  /* Back side */
  .card--back { background: var(--card-dark); color: var(--white); }
  .card--back .wordmark {
    position: absolute; left: 0; right: 0; top: 112px; text-align: center;
    font-weight: 300; font-size: 40px; letter-spacing: 12px; text-transform: uppercase;
    color: var(--white);
  }
  .card--back .website {
    position: absolute; left: 0; right: 0; top: 210px; text-align: center;
    font-size: 15px; letter-spacing: 2px; font-weight: 400;
  }
  /* Front side */
  .card--front { background: var(--card-light); color: var(--ink); }
  .card--front .wordmark {
    position: absolute; right: 44px; top: 54px;
    font-weight: 300; font-size: 28px; letter-spacing: 8px; text-transform: uppercase;
    color: var(--ink);
  }
  .card--front .top-rule {
    position: absolute; left: 44px; right: 44px; top: 108px; height: 1px; background: var(--rule);
  }
  .holder { position: absolute; left: 44px; top: 156px; }
  .holder .name {
    font-weight: 600; font-size: 19px; color: var(--brand-blue); letter-spacing: 0.5px; text-transform: uppercase;
  }
  .holder .role { font-size: 15px; color: var(--ink-soft); margin-top: 4px; }
  .holder-rule {
    position: absolute; left: 44px; width: 230px; top: 212px; height: 1px; background: var(--rule);
  }
  .contacts { position: absolute; left: 44px; top: 224px; list-style: none; }
  .contacts li {
    display: flex; align-items: center; gap: 9px;
    font-size: 15px; line-height: 19px; color: var(--ink-soft);
  }
  .contacts svg { width: 13px; height: 13px; fill: var(--brand-blue); flex: none; }
  .address {
    position: absolute; right: 44px; top: 156px; text-align: right;
    font-size: 14px; line-height: 19px; color: var(--ink-soft);
  }
</style>
</head>
<body>
<main class="stage">
  <section class="card card--back" aria-label="Business card back">
    <div class="wordmark">Corvane Holdings</div>
    <div class="website">www.corvane-demo.ae</div>
  </section>

  <section class="card card--front" aria-label="Business card front">
    <div class="wordmark">Corvane Holdings</div>
    <div class="top-rule"></div>

    <div class="holder">
      <div class="name">Khalid Bin Rashed</div>
      <div class="role">Managing Director</div>
    </div>
    <div class="holder-rule"></div>

    <ul class="contacts">
      <li>
        <svg viewBox="0 0 16 16" aria-hidden="true"><path d="M2 5c0-2 2-3 6-3s6 1 6 3v1h-3V5H5v1H2zM4 7h8l2 7H2z"/></svg>
        +971 4 000 1234
      </li>
      <li>
        <svg viewBox="0 0 16 16" aria-hidden="true"><path d="M4 0h8a1 1 0 0 1 1 1v14a1 1 0 0 1-1 1H4a1 1 0 0 1-1-1V1a1 1 0 0 1 1-1zm1 2v10h6V2zm3 11a1 1 0 1 0 0 2 1 1 0 0 0 0-2z"/></svg>
        +971 50 000 5678
      </li>
      <li>
        <svg viewBox="0 0 16 16" aria-hidden="true"><path d="M0 3h16v1L8 9 0 4zm0 3l8 5 8-5v7H0z"/></svg>
        khalid@corvane-demo.ae
      </li>
      <li>
        <svg viewBox="0 0 16 16" aria-hidden="true"><circle cx="8" cy="8" r="8"/></svg>
        www.corvane-demo.ae
      </li>
    </ul>

    <address class="address" style="font-style:normal">
      Palmgate Tower, officw 18-B07<br>
      Noor Terraces, Dubai
    </address>
  </section>
</main>
</body>
</html>
```